Creative & Professional Business Card for hair salon

We are looking to update our business cards. Our salon is creative, modern, progressive and professional and looking for a design that will reflect this.

```html
<!DOCTYPE html>
<html lang="en">
<head>
<meta charset="utf-8">
<title>Aster Lane Salon – Business Card</title>
<link href="https://fonts.googleapis.com/css2?family=Open+Sans:wght@400;600&family=Raleway:wght@300&display=swap" rel="stylesheet">
<style>
  :root {
    --backdrop: #e9e7e4;
    --card-dark: #0d0d0d;
    --card-light: #ffffff;
    --brand-blue: #5b9db6;
    --brand-blue-soft: #74b1c6;
    --text-grey: #6a6a6a;
    --divider: #d5dde0;
  }
  * { margin: 0; padding: 0; box-sizing: border-box; }
  html, body { width: 1200px; height: 1000px; overflow: hidden; }
  body {
    background: var(--backdrop);
    position: relative;
    font-family: "Open Sans", Arial, sans-serif;
  }
  .card {
    position: absolute;
    left: 266px;
    width: 666px;
    height: 397px;
    box-shadow: 0 3px 8px rgba(0,0,0,0.25);
  }
  .card--front { top: 74px; background: var(--card-dark); }
  .card--back { top: 531px; background: var(--card-light); }

  .brand {
    position: absolute;
    display: flex;
    align-items: center;
    font-family: "Raleway", "Helvetica Neue", sans-serif;
    font-weight: 300;
    white-space: nowrap;
  }
  .brand__dot { border-radius: 50%; flex: none; }
  .card--front .brand {
    left: 0; right: 0; top: 170px;
    justify-content: center;
    gap: 18px;
    font-size: 44px;
    color: var(--brand-blue-soft);
  }
  .card--front .brand__dot { width: 22px; height: 22px; background: var(--brand-blue-soft); }
  .card--back .brand {
    left: 42px; top: 170px;
    gap: 10px;
    font-size: 26px;
    color: var(--brand-blue);
  }
  .card--back .brand__dot { width: 14px; height: 14px; background: var(--brand-blue); }

  .divider {
    position: absolute;
    left: 349px; top: 118px;
    width: 1px; height: 170px;
    background: var(--divider);
  }
  .contact {
    position: absolute;
    left: 374px; top: 118px;
    color: var(--text-grey);
    font-size: 15.5px;
    line-height: 21px;
  }
  .contact__name { color: var(--brand-blue); font-size: 19px; font-weight: 600; line-height: 24px; }
  .contact__role { color: var(--brand-blue); font-size: 15.5px; margin-bottom: 6px; }
  .contact__address { margin-bottom: 6px; }
  .contact__line { display: flex; align-items: center; gap: 5px; }
  .contact__line svg { width: 13px; height: 13px; fill: var(--text-grey); flex: none; }
</style>
</head>
<body>
  <section class="card card--front">
    <div class="brand"><span class="brand__dot"></span>Aster Lane Salon</div>
  </section>

  <section class="card card--back">
    <div class="brand"><span class="brand__dot"></span>Aster Lane Salon</div>
    <div class="divider"></div>
    <div class="contact">
      <p class="contact__name">Daniel Ashford</p>
      <p class="contact__role">CEO / Owner</p>
      <p class="contact__address">218 Linden Avenue<br>Clayton, Missouri 63105</p>
      <p class="contact__line">
        <svg viewBox="0 0 16 16" aria-hidden="true"><path d="M3 2h3l1.5 3.5-2 1.2a8 8 0 0 0 3.8 3.8l1.2-2L14 10v3a1 1 0 0 1-1 1A11 11 0 0 1 2 3a1 1 0 0 1 1-1z"/></svg>
        555-201-4836
      </p>
      <p class="contact__line">
        <svg viewBox="0 0 16 16" aria-hidden="true"><path d="M1 3h14v10H1z M2 4v.4l6 4.2 6-4.2V4z" fill-rule="evenodd"/></svg>
        hello@asterlanesalon.com
      </p>
      <p class="contact__line">
        <svg viewBox="0 0 16 16" aria-hidden="true"><path d="M8 1a7 7 0 1 0 0 14A7 7 0 0 0 8 1zm0 1.5a5.5 5.5 0 0 1 4.6 2.5H10L8.5 6.5 9.5 8 8 10.5 6 9 5 6 3.6 5A5.5 5.5 0 0 1 8 2.5z"/></svg>
        www.asterlanesalon.com
      </p>
    </div>
  </section>
</body>
</html>
```